Bring to life the sophistication and high-level expertise of my consulting business

I am looking for a sleek, modern, sharp PowerPoint design package, with options for a wide range of slide types.
We would like our logo/graphic and its colors (a blue pallet) to be prominently featured. The design should communicate expertise, sophistication, executive-level of work, be bold and look clean and sleek at the same time. There should be no doubt this was professionally done.
The font that will best work with this logo is a basic font using AvantGarde BkBt (custom)
Company briefing:
A consulting and advisory practice specialized in the Consumer Goods and Services Industries. Our methodology is distinguished by its ability to transform visionary thinking—be it blue-sky ideas, inspiration, or innovation—into practical strategies. We drive initiatives aimed at driving revenue growth and enhancing profit margins using 3 pillars: THE PEOPLE, THE CUSTOMER EXPERIENCE and THE OPERATING PLATFORM.
Target audiences are in 3 key areas: C-suite executives (owners and decision-makers of small to mid-cap companies), partners in larger Consulting Companies and Investment Firms (Private Equity/Venture capital, etc)

*In addition to the PowerPoint package, I would like a quote for designs for an email signature, a Microsoft Word template, and a company LinkedIn page (all in the same style as the PPT template)
Updates

Low design quality

Target Market(s)

Target audiences are in 3 key areas: C-suite executives (owners and decision-makers), partners in larger Consulting Companies and Investment Firms (Private Equity/Venture capital, etc.)

Industry/Entity Type

Business Consulting and Advisory

Font styles to use
Sans Serif
Other font styles liked:
• The font that will work best with the logo is basic font using AvantGarde BkBt (custom)

Colors
0054AA
0677BA
7BADD7
CADEEF
E8F1F8
0094D4
00A9DD
6FCCEA
C7EBF8
E9F6FB

Requirements
Must have
• We would like our logo, the graphic shapes and its colors (a blue pallet) to be prominently featured. The design should communicate expertise, sophistication, executive-level of work. It should be sleek, modern, bold and unique.
Nice to have
• A large number of slide options for each type of slide as part of the package
Should not have
• it should not look busy, generic or too traditional

```html
<!DOCTYPE html>
<html lang="en">
<head>
<meta charset="utf-8">
<title>Corvalen Business Marketing Presentation</title>
<link rel="stylesheet" href="https://fonts.googleapis.com/css2?family=Poppins:wght@400;500;600;700&family=Oswald:wght@500;700&display=swap">
<style>
:root{
  --navy:#313f52;
  --cyan:#1db8e4;
  --blue:#1e7fc9;
  --ink:#2b3442;
  --grey:#7a7f86;
  --paper:#ffffff;
  --bg:#e3e4e6;
}
*{margin:0;padding:0;box-sizing:border-box}
html,body{width:1200px;height:1040px;overflow:hidden;background:var(--bg);font-family:"Poppins",sans-serif}
.canvas{position:relative;width:1200px;height:1040px}
.page{position:absolute;width:354px;height:458px;background:var(--paper);box-shadow:0 3px 10px rgba(0,0,0,.18);overflow:hidden}
.abs{position:absolute}
.photo{position:absolute}
.brand{position:absolute;display:flex;align-items:center;gap:4px;font-family:"Poppins",sans-serif;font-weight:500;color:var(--navy);letter-spacing:.22em}
.brand .dot{border-radius:50%;background:var(--cyan);flex:none}
.brand-sm{top:16px;right:12px;font-size:6.5px}
.brand-sm .dot{width:7px;height:7px}
.folio{position:absolute;right:12px;bottom:12px;width:18px;height:18px;border-radius:50%;border:1.5px dotted var(--cyan);font-size:6px;display:flex;align-items:center;justify-content:center;color:var(--ink)}
.heading{position:absolute;left:20px;top:22px;font-size:21px;font-weight:600;color:var(--ink)}
.rule{position:absolute;left:0;top:56px;width:65px;height:3px;background:var(--cyan)}
.body{font-size:6.3px;line-height:1.45;color:var(--grey)}

/* cover */
.cover-square{left:13px;top:12px;width:9px;height:9px;background:var(--navy)}
.cover-panel{left:162px;top:30px;width:192px;height:110px;background:var(--navy);border-top-left-radius:28px}
.cover-kicker{left:179px;top:47px;font-size:12.5px;color:#fff}
.cover-title{left:178px;top:62px;font-family:"Oswald",sans-serif;font-weight:700;font-size:37px;line-height:1;color:var(--cyan);letter-spacing:.01em}
.cover-sub{left:179px;top:106px;font-size:19px;font-weight:600;color:#fff}
.cover-brand{left:28px;top:76px;font-size:11px}
.cover-brand .dot{width:12px;height:12px}
.web-tab{left:0;top:375px;width:160px;height:57px;background:var(--blue);border-bottom-right-radius:20px;color:#fff;font-size:10.5px;letter-spacing:.22em;display:flex;align-items:center;padding-left:14px}
.dots{left:263px;top:416px;display:flex;gap:8px}
.dots span{width:9px;height:9px;border-radius:50%;background:var(--navy)}
.dots span:nth-child(2){background:var(--blue)}

/* agenda */
.agenda-item{position:absolute;left:60px;width:230px}
.agenda-item .num{position:absolute;left:0;top:0;font-size:11px;font-weight:600;color:var(--ink)}
.agenda-item .label{margin-left:15px;font-size:9.5px;font-weight:600;color:var(--blue)}
.agenda-item .body{margin-left:15px;margin-top:2px}

/* subject */
.band-navy{left:0;top:66px;width:354px;height:152px;background:var(--navy)}
.band-cyan{left:0;top:218px;width:354px;height:97px;background:var(--cyan)}
.subject-title{left:146px;top:62px;font-size:18px;font-weight:600;color:#fff}
.subject-rule{left:146px;top:103px;width:35px;height:3px;background:var(--cyan)}
.subject-copy{left:146px;top:114px;width:192px;color:#e8edf2}
.subject-copy p+p{margin-top:6px}
.subject-lead{left:17px;top:260px;font-size:15.5px;font-weight:600;color:var(--navy);line-height:1.4}
.subject-note{left:20px;top:325px;width:170px;font-size:7.6px}
.subject-note p+p{margin-top:6px}

/* about */
.about-copy{left:15px;top:73px;width:175px}
.about-copy p+p{margin-top:7px}
.about-band{left:0;top:266px;width:354px;height:144px;background:var(--navy)}
.point{position:absolute;width:140px;font-size:8px;line-height:1.18;color:#fff;letter-spacing:.02em}
.point svg{position:absolute;left:-20px;top:1px}

/* features */
.feature-band{left:0;top:70px;width:354px;height:196px;background:var(--navy)}
.feature{position:absolute;width:80px;text-align:center;color:#fff}
.feature .icon{width:32px;height:32px;margin:0 auto;background:var(--cyan);border:1.5px solid #fff;display:flex;align-items:center;justify-content:center}
.feature .label{font-size:8px;font-weight:600;margin-top:9px}
.feature .body{color:#cfd6de;font-size:4.6px;line-height:1.3}
.text-head{left:28px;top:270px;font-size:12px;font-weight:500;color:var(--ink)}
.text-copy{left:28px;top:289px;width:312px;font-size:5.6px}
.text-copy p+p{margin-top:6px}
.step{position:absolute;top:368px;width:130px}
.step .badge{position:absolute;left:0;top:0;width:20px;height:20px;background:var(--blue);color:#fff;font-size:12px;font-weight:600;display:flex;align-items:center;justify-content:center}
.step .txt{margin-left:29px}
.step .label{font-size:8.5px;font-weight:500;color:var(--ink)}
.step .body{font-size:5.4px;line-height:1.3}

/* thank you */
.end-brand{left:0;width:354px;top:70px;justify-content:center;font-size:17px}
.end-brand .dot{width:14px;height:14px}
.vbar{left:277px;top:141px;width:44px;height:206px;background:var(--cyan)}
.vbar span{position:absolute;left:50%;top:50%;transform:translate(-50%,-50%) rotate(-90deg);color:#fff;font-size:12px;letter-spacing:.25em;white-space:nowrap}
.thanks{left:29px;top:372px;font-size:40px;font-weight:700;color:var(--navy);letter-spacing:-.01em}
.end-square{left:323px;top:428px;width:13px;height:13px;background:var(--cyan)}
</style>
</head>
<body>
<main class="canvas">

  <!-- Cover -->
  <section class="page" style="left:48px;top:52px">
    <div class="abs cover-square"></div>
    <div class="brand cover-brand"><span class="dot"></span>CORVALEN</div>
    <div class="abs cover-panel"></div>
    <div class="abs cover-kicker">PRESENTATION</div>
    <div class="abs cover-title">BUSINESS</div>
    <div class="abs cover-sub">MARKETING</div>
    <div class="photo" role="img" aria-label="Businesswoman on the phone working at a laptop in a bright office" style="left:0;top:140px;width:354px;height:235px;background:linear-gradient(100deg,#eef0ef 0%,#d9dcdc 45%,#8fc2b3 65%,#e4e6e6 100%)"></div>
    <div class="abs web-tab">www.website.com</div>
    <div class="abs dots"><span></span><span></span><span></span></div>
  </section>

  <!-- Agenda -->
  <section class="page" style="left:422px;top:52px">
    <h2 class="heading">Agenda</h2>
    <div class="rule"></div>
    <div class="brand brand-sm"><span class="dot"></span>CORVALEN</div>
    <div class="agenda-item" style="top:100px"><span class="num">1.</span><div class="label">Lorem ipsum</div><p class="body">Lorem ipsum dolor sit amet, consectetuer adipiscing elit, sed diam nonummy nibh euismod tincid</p></div>
    <div class="agenda-item" style="top:144px"><span class="num">2.</span><div class="label">Lorem ipsum</div><p class="body">Lorem ipsum dolor sit amet, consectetuer adipiscing elit, sed diam nonummy nibh euismod tincid</p></div>
    <div class="agenda-item" style="top:191px"><span class="num">3.</span><div class="label">Lorem ipsum</div><p class="body">Lorem ipsum dolor sit amet, consectetuer adipiscing elit, sed diam nonummy nibh euismod tincid</p></div>
    <div class="agenda-item" style="top:237px"><span class="num">4.</span><div class="label">Lorem ipsum</div><p class="body">Lorem ipsum dolor sit amet, consectetuer adipiscing elit, sed diam nonummy nibh euismod tincid</p></div>
    <div class="agenda-item" style="top:286px"><span class="num">5.</span><div class="label">Lorem ipsum</div><p class="body">Lorem ipsum dolor sit amet, consectetuer adipiscing elit, sed diam nonummy nibh euismod tincid</p></div>
    <div class="agenda-item" style="top:335px"><span class="num">6.</span><div class="label">Lorem ipsum</div><p class="body">Lorem ipsum dolor sit amet, consectetuer adipiscing elit, sed diam nonummy nibh euismod tincid</p></div>
    <div class="folio">2</div>
  </section>

  <!-- Subject -->
  <section class="page" style="left:798px;top:52px">
    <div class="brand brand-sm"><span class="dot"></span>CORVALEN</div>
    <div class="abs band-navy"></div>
    <div class="abs band-cyan"></div>
    <div class="photo" role="img" aria-label="Two colleagues reviewing work on a laptop" style="left:19px;top:39px;width:113px;height:212px;background:linear-gradient(170deg,#dfe3e6 0%,#9aa6b2 45%,#4d6079 75%,#c9ccd0 100%)"></div>
    <h2 class="abs subject-title">Subject Title</h2>
    <div class="abs subject-rule"></div>
    <div class="abs subject-copy body"><p>Lorem ipsum dolor sit amet, consectetuer adipiscing elit, sed diam nonummy nibh euismod tincidunt ut laoreet dolore magna aliquam</p><p>erat volutpat. Ut wisi enim ad minim veniam, quis nostrud exerci tation ullamcorper suscipit lobortis nisl ut aliquip ex ea commodo consequat. Duis autem vel eum iriure.</p></div>
    <div class="photo" role="img" aria-label="Two coworkers talking by an office window" style="left:204px;top:197px;width:127px;height:208px;background:linear-gradient(180deg,#e9eef2 0%,#c7d3dd 40%,#f2f3f4 60%,#2d3c55 100%)"></div>
    <div class="abs subject-lead">Lorem Ipsum<br>Dolor Sit Ametkeeper.</div>
    <div class="abs subject-note body"><p>Lorem ipsum dolor sit amet, consectetuer adipiscing</p><p>elit, sed diam nonummy nibh euismod tincidunt ut laoreet dolore magna aliquam erat volutpat. Ut wisi enim ad minim veniam,quis nostrud exerci tation</p></div>
    <div class="folio">3</div>
  </section>

  <!-- About -->
  <section class="page" style="left:48px;top:530px">
    <h2 class="heading">About Us</h2>
    <div class="rule"></div>
    <div class="brand brand-sm"><span class="dot"></span>CORVALEN</div>
    <div class="abs about-copy body"><p>Lorem ipsum dolor sit amet, consectetuer adipiscing elit, sed diam nonummy nibh euismod tincidunt ut laoreet dolore magna aliquam erat volutpat. Ut wisi enim ad minim veniam, quis nostrud exerci tation ullamcorper suscipit lobortis nisl ut aliquip.</p><p>Ex ea commodo consequat. Duis autem vel eum iriure dolor in hendrerit in vulputate velit esse molestie consequat, vel illum dolore eu feugiat nulla facilisis at vero eros et accumsan et iusto odio dignissim qui blandit praesent luptatum zzril delenit augue duis dolore te feugait nulla facilisi.Lorem ipsum dolor sit amet, cons ectetuer adipiscing elit, sed diam nonummy nibh euismod tincidunt ut laoreet dolore magna aliquam erat volutpat. Ut wisi enim ad minim veniam, quis nostrud exerci tation ullamcorper suscipit lobortis nisl ut aliquip ex ea commodo cons</p></div>
    <div class="photo" role="img" aria-label="Overhead view of business people shaking hands in a lobby" style="left:196px;top:66px;width:158px;height:200px;background:linear-gradient(135deg,#eef1f4 0%,#cfd6de 40%,#6f7c8c 70%,#e1e5ea 100%)"></div>
    <div class="abs about-band"></div>
    <div class="point" style="left:40px;top:284px"><svg width="10" height="11" viewBox="0 0 10 11"><path d="M0 0L10 5.5 0 11z" fill="#1db8e4"/></svg>Lorem ipsum dolor sit amet, consectetuer adipis-cing elit, sed diam nonum-my nibh euismod tincidunt ut laoreet dolore magna</div>
    <div class="point" style="left:212px;top:287px"><svg width="10" height="11" viewBox="0 0 10 11"><path d="M.7 1.2L8.6 5.5 .7 9.8z" fill="none" stroke="#1db8e4" stroke-width="1"/></svg>Lorem ipsum dolor sit amet, consectetuer adipis-cing elit, sed diam nonum-my nibh euismod tincidunt ut laoreet dolore magna</div>
    <div class="point" style="left:40px;top:358px"><svg width="10" height="11" viewBox="0 0 10 11"><path d="M.7 1.2L8.6 5.5 .7 9.8z" fill="none" stroke="#1db8e4" stroke-width="1"/></svg>Lorem ipsum dolor sit amet, consectetuer adipis-cing elit, sed diam nonum-my nibh euismod tincidunt ut laoreet dolore magna</div>
    <div class="point" style="left:212px;top:356px"><svg width="10" height="11" viewBox="0 0 10 11"><path d="M0 0L10 5.5 0 11z" fill="#1db8e4"/></svg>Lorem ipsum dolor sit amet, consectetuer adipis-cing elit, sed diam nonum-my nibh euismod tincidunt ut laoreet dolore magna</div>
    <div class="folio">4</div>
  </section>

  <!-- Text Added -->
  <section class="page" style="left:422px;top:530px">
    <h2 class="heading">Text Added</h2>
    <div class="rule"></div>
    <div class="brand brand-sm"><span class="dot"></span>CORVALEN</div>
    <div class="abs feature-band"></div>
    <div class="feature" style="left:21px;top:87px"><div class="icon"><svg width="20" height="16" viewBox="0 0 20 16" fill="none" stroke="#fff" stroke-width="1"><circle cx="5" cy="5" r="2.5"/><circle cx="10" cy="4" r="2.5"/><circle cx="15" cy="5" r="2.5"/><path d="M1 14c0-3 2-5 4-5s4 2 4 5M6 14c0-3 2-5 4-5s4 2 4 5M11 14c0-3 2-5 4-5s4 2 4 5"/></svg></div><div class="label">Lorem ipsum</div><p class="body">Lorem ipsum dolor sit amet, consectetuer adipiscing elit, sed diam nonummy nibh euismod tincidunt ut laoreet</p></div>
    <div class="feature" style="left:137px;top:87px"><div class="icon"><svg width="20" height="18" viewBox="0 0 20 18" fill="none" stroke="#fff" stroke-width="1"><circle cx="7" cy="9" r="5"/><circle cx="15" cy="5" r="3.5"/><circle cx="11" cy="14" r="2.5"/></svg></div><div class="label">Lorem ipsum</div><p class="body">Lorem ipsum dolor sit amet, consectetuer adipiscing elit, sed diam nonummy nibh euismod tincidunt ut laoreet</p></div>
    <div class="feature" style="left:253px;top:87px"><div class="icon"><svg width="20" height="18" viewBox="0 0 20 18" fill="none" stroke="#fff" stroke-width="1"><rect x="3" y="11" width="3" height="6"/><rect x="8" y="8" width="3" height="9"/><rect x="13" y="5" width="3" height="12"/><path d="M2 8l6-4 3 2 7-5M15 1h3v3"/></svg></div><div class="label">Lorem ipsum</div><p class="body">Lorem ipsum dolor sit amet, consectetuer adipiscing elit, sed diam nonummy nibh euismod tincidunt ut laoreet</p></div>
    <div class="feature" style="left:21px;top:176px"><div class="icon"><svg width="20" height="18" viewBox="0 0 20 18" fill="none" stroke="#fff" stroke-width="1"><path d="M2 1v16h17M5 5c2 6 6 9 12 9M14 11l3 3-3 2"/></svg></div><div class="label">Lorem ipsum</div><p class="body">Lorem ipsum dolor sit amet, consectetuer adipiscing elit, sed diam nonummy nibh euismod tincidunt ut laoreet</p></div>
    <div class="feature" style="left:137px;top:176px"><div class="icon"><svg width="18" height="20" viewBox="0 0 18 20" fill="none" stroke="#fff" stroke-width="1"><path d="M6 1h6l-2 4h-2zM8 5C3 8 1 12 2 16c1 3 13 3 14 0 1-4-1-8-6-11"/><text x="6.5" y="15" font-size="7" fill="#fff" stroke="none" font-family="Poppins,sans-serif">$</text></svg></div><div class="label">Lorem ipsum</div><p class="body">Lorem ipsum dolor sit amet, consectetuer adipiscing elit, sed diam nonummy nibh euismod tincidunt ut laoreet</p></div>
    <div class="feature" style="left:253px;top:176px"><div class="icon"><svg width="20" height="20" viewBox="0 0 20 20" fill="none" stroke="#fff" stroke-width="1"><circle cx="10" cy="8" r="6"/><circle cx="10" cy="8" r="3.5"/><path d="M6 13l-2 6 3-1 2 2 1-4M14 13l2 6-3-1-2 2-1-4"/></svg></div><div class="label">Lorem ipsum</div><p class="body">Lorem ipsum dolor sit amet, consectetuer adipiscing elit, sed diam nonummy nibh euismod tincidunt ut laoreet</p></div>
    <h3 class="abs text-head">1. Text Added Here</h3>
    <div class="abs text-copy body"><p>Lorem ipsum dolor sit amet, cons ectetuer adipiscing elit, sed diam nonummy nibh euismod tincidunt ut laoreet dolore magna aliquam erat volutpat. Ut wisi enim ad minim veniam, quis nostrud exerci tation ullamcorper suscipit lobortis nisl ut aliquip ex ea commodo consequat.</p><p>Lorem ipsum dolor sit amet, consectetuer adipiscing elit, sed diam nonummy nibh euismod tincidunt ut laoreet dolore magna aliquam erat volutpat. Ut wisi enim ad minim veniam, quis nostrud exerci tation ullamcorper suscipit lobortis nisl ut aliquip ex ea commodo consequat.</p></div>
    <div class="step" style="left:47px"><div class="badge">1.</div><div class="txt"><div class="label">Lorem ipsum</div><p class="body">Lorem ipsum dolor sit amet, consectetuer adipiscing elit, sed diam nonummy nibh euismod tincid</p></div></div>
    <div class="step" style="left:191px"><div class="badge">2.</div><div class="txt"><div class="label">Lorem ipsum</div><p class="body">Lorem ipsum dolor sit amet, consectetuer adipiscing elit, sed diamnonummy nibh euismod tincid</p></div></div>
    <div class="folio">5</div>
  </section>

  <!-- Thank You -->
  <section class="page" style="left:798px;top:530px">
    <div class="brand end-brand"><span class="dot"></span>CORVALEN</div>
    <div class="photo" role="img" aria-label="Team meeting around a table with a presenter pointing at a monitor" style="left:0;top:141px;width:268px;height:206px;background:linear-gradient(160deg,#cfd5db 0%,#8d9bab 35%,#4e5f73 60%,#e7e9ec 100%)"></div>
    <div class="abs vbar"><span>www.website.com</span></div>
    <div class="abs thanks">Thank You</div>
    <div class="abs end-square"></div>
  </section>

</main>
</body>
</html>
```